Mindfulness School for Children -- Business Cards

We're looking for business cards for our school directors and owners. We're a mindfulness school for children called tumbling willows. Attached are our logos/icons.

```html
<!DOCTYPE html>
<html lang="en">
<head>
<meta charset="utf-8">
<title>Tumbling Willows Business Card</title>
<link href="https://fonts.googleapis.com/css2?family=Karla:wght@400;500;700&display=swap" rel="stylesheet">
<style>
  :root {
    --backdrop: #8f8f8f;
    --card-white: #ffffff;
    --teal: #44a5b7;
    --green: #86c797;
    --brand: #5db4ad;
    --text: #4e5254;
    --icon: #5aa89a;
    --pattern-light: #45e4f6;
    --pattern-mid: #2ba2bb;
    --pattern-dark: #0c5d86;
    --watermark: rgba(180, 215, 222, 0.22);
  }
  * { margin: 0; padding: 0; box-sizing: border-box; }
  html, body { width: 1200px; height: 1200px; overflow: hidden; }
  body { background: var(--backdrop); font-family: "Karla", sans-serif; position: relative; }

  .card {
    position: absolute;
    left: 262px;
    width: 686px;
    height: 392px;
    border-radius: 20px;
    overflow: hidden;
  }
  .card-front { top: 165px; background: var(--card-white); }
  .card-back { top: 653px; }

  .front-watermark {
    position: absolute;
    left: 0; top: 30px;
    width: 370px; height: 360px;
    background: radial-gradient(ellipse at 40% 55%, var(--watermark) 0%, rgba(180,215,222,0.12) 55%, rgba(255,255,255,0) 75%);
  }

  .brand-name {
    position: absolute;
    right: 40px; top: 62px;
    font-size: 36px;
    font-weight: 400;
    color: var(--brand);
    letter-spacing: -0.5px;
    display: flex; align-items: center; gap: 8px;
  }
  .brand-dot { width: 12px; height: 12px; border-radius: 50%; background: var(--brand); }

  .person-name {
    position: absolute; left: 45px; top: 137px;
    font-size: 22px; font-weight: 500; letter-spacing: 1px;
    color: var(--teal);
  }
  .person-title {
    position: absolute; left: 45px; top: 165px;
    font-size: 15px; letter-spacing: 0.8px; color: var(--green);
  }
  .address {
    position: absolute; left: 46px; top: 205px;
    font-size: 15px; line-height: 19px; color: var(--text); letter-spacing: 0.3px;
  }
  .contact-list {
    position: absolute; left: 47px; top: 261px;
    list-style: none; font-size: 15px; color: var(--text); letter-spacing: 0.3px;
  }
  .contact-list li { height: 19.4px; display: flex; align-items: center; gap: 10px; }
  .contact-list svg { width: 13px; height: 13px; fill: var(--icon); flex: none; }

  .accent-bands { position: absolute; left: 0; bottom: 0; width: 686px; height: 15px; }

  .back-pattern {
    position: absolute; inset: 0;
    background:
      linear-gradient(100deg, var(--pattern-light) 0%, var(--pattern-mid) 45%, var(--pattern-dark) 100%);
  }
</style>
</head>
<body>
  <section class="card card-front">
    <div class="front-watermark" role="img" aria-label="Faint brand mark watermark area"></div>

    <div class="brand-name"><span class="brand-dot"></span>tumbling willows</div>

    <h1 class="person-name">DANIEL REYES</h1>
    <p class="person-title">President</p>

    <p class="address">4120 Birchwood Lane<br>Fairbanks, Alaska 99701</p>

    <ul class="contact-list">
      <li><svg viewBox="0 0 16 16" aria-hidden="true"><path d="M3.5 1l3 3-1.8 1.8a9 9 0 0 0 5.5 5.5L12 9.5l3 3-2 2.5C7 15 1 9 1 3z"/></svg>555-204-7731</li>
      <li><svg viewBox="0 0 16 16" aria-hidden="true"><path d="M4 0h8a1 1 0 0 1 1 1v14a1 1 0 0 1-1 1H4a1 1 0 0 1-1-1V1a1 1 0 0 1 1-1zm1 2v10h6V2zm3 11a1 1 0 1 0 0 2 1 1 0 0 0 0-2z"/></svg>555-418-2260</li>
      <li><svg viewBox="0 0 16 16" aria-hidden="true"><path d="M4 1h6l2 2v4H4zM1 8h14v6H1zm3 2v2h8v-2z"/></svg>555-391-5084</li>
      <li><svg viewBox="0 0 16 16" aria-hidden="true"><path d="M1 3h14v10H1zm1.5 1.2L8 8.5l5.5-4.3z"/></svg>info@tumblingwillows.com</li>
      <li><svg viewBox="0 0 16 16" aria-hidden="true"><path d="M8 1a7 7 0 1 0 0 14A7 7 0 0 0 8 1zm-1 2.5c1 .5 1.5 1.5 1 2.5s-2 1-2.5 2 .5 2 0 3.5C3.5 10 3 6 7 3.5zm3 7c.5-1 2-1.5 3-1a5 5 0 0 1-3 3.5z"/></svg>www.tumblingwillows.com</li>
    </ul>

    <svg class="accent-bands" viewBox="0 0 686 15" preserveAspectRatio="none" aria-hidden="true">
      <polygon points="0,0 339,0 335,15 0,15" fill="var(--green)"/>
      <polygon points="344,0 686,0 686,15 340,15" fill="var(--teal)"/>
    </svg>
  </section>

  <section class="card card-back">
    <div class="back-pattern" role="img" aria-label="Repeating lotus flower pattern in graduated teal tones"></div>
  </section>
</body>
</html>
```